Business Card Design - TWM (company name)

Over 20 years of progressive technology design, migration and management experience that drives business objectives and streamlines operations. Continuously challenge conventions to meet and exceed business security, availability and functionality requirements. Maintain exceptional vendor relationships to ensure ongoing knowledge of emerging products and to secure preferred service agreements. Recruit and utilize top talent and foster a collegial environment that advances innovation and performance excellence. design logo using 3 arrows of different colors green, gold, blue

Industry/Entity Type

Progressive

Contact Information for Business Card

Martin K. Osei
IT Strategist / Consultant

626.583.2097 MOsei@twmosei.com 4817 Brantley Court Pasadena, CA 91107

Colors
0255a3
f37122
fece3e

Requirements
Must have
• Note NEW EMAIL ADDRESS
• MOsei@twmosei.com
• NOTE NEW ORDER of the work I do.
• Infrastructure – Systems – Cybersecurity
Nice to have
• main color should be orange

```html
<!DOCTYPE html>
<html lang="en">
<head>
<meta charset="utf-8">
<title>Martin K. Osei – Business Card</title>
<link rel="stylesheet" href="https://fonts.googleapis.com/css2?family=Oswald:wght@700&family=PT+Sans+Narrow:wght@400;700&display=swap">
<style>
  :root {
    --bg: #e9e9e9;
    --card: #ffffff;
    --peach: #fed28c;
    --orange: #f37122;
    --orange-light: #f7941d;
    --ink: #111111;
    --white: #ffffff;
    --icon: #fde0b0;
  }
  * { margin: 0; padding: 0; box-sizing: border-box; }
  html, body { width: 1200px; height: 1000px; overflow: hidden; background: var(--bg); }
  .canvas { position: relative; width: 1200px; height: 1000px; }

  .card {
    position: absolute;
    width: 600px;
    height: 340px;
    background: var(--card);
    overflow: hidden;
    box-shadow: 0 4px 14px rgba(0,0,0,0.18);
  }
  .card--back { left: 60px; top: 110px; }
  .card--front { left: 540px; top: 550px; }

  .band { position: absolute; top: 0; height: 100%; background: var(--peach); }
  .card--back .band { left: 0; width: 220px; }
  .card--front .band { right: 0; width: 250px; }

  .slab-accent { position: absolute; background: var(--orange-light); }
  .slab { position: absolute; background: var(--orange); color: var(--white); }

  .card--back .slab-accent { left: 0; top: 60px; width: 262px; height: 196px; }
  .card--back .slab { left: 0; top: 78px; width: 292px; height: 160px; }

  .card--front .slab-accent { right: 0; top: 110px; width: 326px; height: 196px; }
  .card--front .slab { right: 0; top: 128px; width: 356px; height: 160px; }

  .specialties {
    position: absolute; left: 96px; top: 26px;
    font-family: "PT Sans Narrow", sans-serif;
    font-size: 20px; line-height: 24px;
  }
  .specialties h3 { font-weight: 700; font-size: 21px; }
  .specialties li { list-style: none; }
  .specialties li:nth-child(1) { padding-left: 8px; }
  .specialties li:nth-child(2) { padding-left: 24px; }
  .specialties li:nth-child(3) { padding-left: 40px; }

  .identity { position: absolute; }
  .card--back .identity { left: 318px; top: 118px; }
  .card--front .identity { left: 40px; top: 78px; }
  .name {
    font-family: "Oswald", sans-serif; font-weight: 700;
    font-size: 40px; line-height: 44px; color: var(--ink);
    text-transform: uppercase; letter-spacing: -0.5px; white-space: nowrap;
  }
  .role {
    font-family: "PT Sans Narrow", sans-serif; font-weight: 400;
    font-size: 22px; line-height: 24px; color: var(--orange-light);
    white-space: nowrap;
  }

  .contacts {
    position: absolute; left: 22px; top: 38px;
    font-family: "PT Sans Narrow", sans-serif; font-size: 17px; line-height: 28px;
  }
  .contacts li { list-style: none; display: flex; align-items: center; gap: 9px; white-space: nowrap; }
  .contacts svg { width: 15px; height: 15px; flex: none; fill: var(--icon); }
</style>
</head>
<body>
<main class="canvas">

  <section class="card card--back">
    <div class="band"></div>
    <div class="slab-accent"></div>
    <div class="slab">
      <div class="specialties">
        <h3>Specialising in:</h3>
        <ul>
          <li>- Infrastructure</li>
          <li>- Systems</li>
          <li>- Cybersecurity</li>
        </ul>
      </div>
    </div>
    <div class="identity">
      <h1 class="name">Martin K. Osei</h1>
      <p class="role">IT Strategist / Consultant</p>
    </div>
  </section>

  <section class="card card--front">
    <div class="band"></div>
    <div class="slab-accent"></div>
    <div class="slab">
      <ul class="contacts">
        <li>
          <svg viewBox="0 0 16 16" aria-hidden="true"><path d="M3.6 1.2l2.3 2.6-1.3 1.8c.9 2 2.6 3.7 4.6 4.6l1.8-1.3 2.6 2.3-1.2 2.3C7.3 13.3 2.7 8.7 1.3 3.6z"/></svg>
          626.583.2097
        </li>
        <li>
          <svg viewBox="0 0 16 16" aria-hidden="true"><path d="M1 3h14v10H1z M2 4l6 5 6-5" stroke="#f37122" stroke-width="1"/></svg>
          MOsei@twmosei.com
        </li>
        <li>
          <svg viewBox="0 0 16 16" aria-hidden="true"><path d="M8 1a5 5 0 0 1 5 5c0 3.5-5 9-5 9S3 9.5 3 6a5 5 0 0 1 5-5zm0 3a2 2 0 1 0 0 4 2 2 0 0 0 0-4z"/></svg>
          4817 Brantley Court Pasadena, CA 91107
        </li>
      </ul>
    </div>
    <div class="identity">
      <h2 class="name">Martin K. Osei</h2>
      <p class="role">IT Strategist / Consultant</p>
    </div>
  </section>

</main>
</body>
</html>
```